Web Design Peartreegrove

Overview: To develop web site with 1 main page and 1 sample inside page. Site already exists, but has been put offline. Content has been fully rewritten. If I like your style, I will pay extra for additional inside pages.
WHO I AM?
www.peartreegrove.example was originally created to become an online community for people to use my online tools, researches, and findings to learn how to become happier.
Today, my primary services is “health coaching and lifestyle specialist.” I’m a food specialist suggesting customized solutions for my clients to eat better, how to eat, cook, groceries shop, lose weight, reduce craving, and reverse diseases.
My edge is when a suggest food I explain Why such food hurts them (or make them sick –or reason of diseases) or how the food I suggest can heal them, strengthen them, or make them lose weight. My connection to food is medical and directly impacts my client’s health.
I want to be seen as a professional in clinical nutrition and as a guru in overall wellbeing.
I coach my clients’ lifestyle as a WHOLE, introducing them to new food, fitness, and teaching them techniques to better cope with life. I study their overall health, history, and treatments, diseases, allergies as a WHOLE, connecting all medical specialties.
My services:
I sell coaching sessions, for 1 hour, 2/month for a total program of 6 months. During the sessions, I not only coach client on nutrition, but also on career, relationship, fitness, goals, and the reasons why people can’t achieve their dreams, or how to remove stress or re-organize their lives.
Future services: I may want to sell products such as T-shirts and other promotional items
Payment methods: Since I sell, I’ll need coinlatch and credit card payment on line. I accept checks as well (they can find my address on “contact us”)
More services, near future:
As a Certified personal fitness Trainer, I will soon offer circuit training (outdoors) and boot camps in the neighborhood to get people moving, at very affordable prices. The goal of those events will be to grow my peartreegrove community and get new clients for Health coaching.
Knowledgeable about controlling the mind, anger, and stress, I will soon offer group meditations and breathing sessions .
Objectives:
The goal of the site are:
• To entice visitors to become my clients. The look of the site needs to reflect my customized services.
• To offer to spend an hour with client for a free health history.
• To post videos about cooking videos, discussing a theme (sugar craving, which Carbs is good for me?)
• After I meet people and give them my business cards, as they visit my site, they needs to feel impressed by the caliber of expertise.
Schedules and Budget:
Target due date is 1 week from submission of my project. During that phase, I’d like to see a wireframe, colors, styles, incorporating my logo, suggesting pictures. I would like designed tabs, access to videos, and photo library.
Motivations for people to become CLIENTS:
I think what would make people want to get my services is if they see me as an expert in holistic weight loss, someone that they can share their life, thrust, and speak at length without being judged. Visuals are crucial to simply explain effect of food on the body (needs videos main page and archive videos on various topics)
Overall, the emotions we can play with - (key words) feeling energized, feeling strong, in control of your life, a holitistic approach to a new healthy lifestyle, Balance mind, fitness, and diet, take responsibility for your own life, feeling lighter, happier, more peaceful.
Key issues of my clients:
Weight issues, high blood pressure, depression, anxiety, stress, don’t know and what to cook, suffer from diabetes, celiac, digestive diseases. People are fatigued or can’t sleep. They are addicted to sugar, coffee, fast food, speedy life.
Another issue is finding time to eat better, making exercise a routine, making the time to remove stress and enjoy life.
How do I solve clients’ problems?:
Rather than being treated by various medical specialists, I look over their Overall health since childhood. I try to find triggers of their sicknesses that often originate from their lifestyle (stress, lack of exercise, eating junk, allergies) and I recommend life modification, introduce new food, exercise , and help them shuffle their lives around. My approach is extremely customized and always requires Hours of research on my side to fully guide a client.
Demographics:
Teenagers, singles, families, young mothers. Most of clients come with weight issues, some may come to reduce cravings.
Key Messages:
The main page (please find attached “wireframe”) shall give the visitor a sense he found the guru in holistic health. Whatever medical concern they have or struggle will finally be taken care of. Someone loves them and truly cares. Food knowledge is medical, flavor, and based on client’s own taste and willingness to try. The overall feel needs to be sleek and professional.
Call to Action
Ideally, I want people to e-mail me their filled up health history (can download blank men or women health history form) so I can schedule an appointment with them (the best solution for me)
People can also call me. Since calling me is for general questions about my program, I would prefer the e-mail version whereby clients send me their health history.
Creative Considerations
Layout – considerations in accordance to brand guidelines
Need suggetions!
Tone –
Expert in clinical food and holistic health.
Visual
Color palette : I’m not sure, but the background could be light gray (clinical health), golden desert, sahara desert, earthy, pottery (well being) warm colors (orange to warm brown) or other suggestion?
Photography: I thought about flash picture. 1 picture as banner with a message on it. About 3 pictures rotate randomly.
Picture A: is “holistic food, green vegetables, natural edible roots, or cruciferous vegetables, a platter of fresh fruits and vegies, or fresh market (spices, roots, fruits and vegies). Picture needs to be crisp clear.
Picture B: Ideally: a lady fitness trainer training group exercise outdoors, in a park, or a group of people exercising outside, people look happy, boot camp training, circuit training as a group
Picture C: a picture representing the soul ,meditation, a person relaxing next to beach or in forest, next to flowers or lushy plants, a person re-energizing.
Logo: attached as separate files with various backgrounds
Icons: may look cool to use vegies or weight, happy face, or ginger root…
typography, graphics: need suggestions!

Resources
• I have an existing website name “peartreegrove.example” the site has been put out of internet since we were trying to change it. Let me know if you need to access site. Content of the site is ineffective.
• All content has been written. You can suggest layouts and tabs
Updates

Target Market(s)

My industry is Health care, holistic Health (no medications, no supplements, no surgeries)
Buyer’s Type could be anyone wanting to lose weight, feel better, reduce stress, learn to eat, to cook, to groceries shop. My buyers are confused about all diets.My audience is people WHO WANT change in their lives. Some people know they should eat better, they mostly need support and motivation.
Typical buyer is someone who wants a new chance, a new life!
My primary target buyer is:
1. Family. I wish to coach the entire family into healthier eating and teach them how to cook and eat as a family by changing their habits.
My secondary markets are:
1.Teenagers (often eating emotionally and confused about diets)

Industry/Entity Type

Requirements
Must have
• • Format – web, print, video, sound
I would like videos (clipvane connect) – friendloom connect – calendar (I will update) – I will update my content, videos, and photo library regularly – people should be able to e-mail me from site – maybe be able to go through web conference. 2 different words or pdf forms shall be available for download or online filling, then they should be able to e-mail forms through site or through their personal mail system. They can also print and mail it to me.
Managing the site:
I would like to upload videos, pictures and text freely and easily. I would like to manage and update content
Nice to have
• would look cool to use entire background as a super picture!

```html
<!DOCTYPE html>
<html lang="en">
<head>
<meta charset="utf-8">
<title>Peartreegrove – Balanced Nutrition, Mind, and Fitness</title>
<link href="https://fonts.googleapis.com/css2?family=Arimo:wght@400;700&family=Archivo+Narrow:wght@700&family=Francois+One&family=Tinos&display=swap" rel="stylesheet">
<style>
:root{
  --cream:#f5f2e4;
  --panel:#ede4c9;
  --panel-edge:#5a4a32;
  --orange:#f7931e;
  --orange-deep:#f26a0f;
  --orange-box:#f7a93b;
  --green:#7cc123;
  --green-deep:#4f9a12;
  --gray-bg:#d9d9d6;
  --ink:#222;
  --text:#444;
  --muted:#777;
  --footer:#3b3b3b;
  --yellow:#ffd200;
  --white:#fff;
}
*{box-sizing:border-box;margin:0;padding:0}
html,body{width:777px;height:1200px;overflow:hidden}
body{position:relative;background:var(--gray-bg);font-family:"Arimo",Arial,sans-serif;color:var(--text)}
.abs{position:absolute}
.top-zone{left:0;top:0;width:777px;height:600px;background:var(--cream)}
.side-leaf{top:190px;width:12px;height:410px;background:linear-gradient(180deg,#cfe7a3,#7cc123)}
.brand{left:20px;top:30px;display:flex;align-items:center;gap:10px}
.brand-mark{width:62px;height:62px;border-radius:50%;background:var(--green)}
.brand-name{font-family:"Arimo",Arial,sans-serif;font-size:32px;font-weight:700;color:var(--green-deep);line-height:1}
.brand-sub{font-size:9px;font-weight:700;letter-spacing:.5px;color:#444;margin-top:4px}
.tagline{right:14px;top:30px;font-size:13px;color:var(--ink)}
.tagline a{color:var(--orange-deep);text-decoration:none}
.search{left:550px;top:89px;width:219px;height:24px;background:var(--white);border:1px solid #bbb;font-size:11px;color:#aaa;padding:5px 7px}
.search svg{position:absolute;right:4px;top:3px}
.stage{left:10px;top:133px;width:759px;height:462px;background:var(--panel);border:3px solid var(--panel-edge);border-top-width:4px}
.nav{left:10px;top:133px;width:759px;height:62px;border-bottom:2px solid var(--panel-edge);display:flex;padding:16px 0 0 24px}
.nav-item{width:147px;font-family:"Archivo Narrow",Arial,sans-serif;font-weight:700;font-size:18px;color:var(--ink);line-height:1}
.nav-item small{display:block;font-family:"Arimo",Arial,sans-serif;font-size:8.5px;font-weight:400;margin-top:2px}
.nav-item.active{color:var(--orange)}
.nav-item.active small{color:var(--ink)}
.thumb{top:210px;width:141px;height:70px;background:var(--white);padding:3px;box-shadow:0 1px 3px rgba(0,0,0,.35)}
.thumb .ph{width:100%;height:100%;position:relative}
.thumb .play{position:absolute;left:50%;top:22px;transform:translateX(-50%)}
.thumb span{position:absolute;bottom:4px;left:0;right:0;text-align:center;font-family:"Francois One",Arial,sans-serif;font-size:12.5px;color:var(--orange)}
.thumb span.g{color:var(--green)}
.slider{left:24px;top:292px;width:731px;height:285px;border:4px solid #8a8f8c;background:linear-gradient(180deg,#4b8fcf 0%,#9cc6e6 30%,#2fb3a8 40%,#1e9a93 62%,#d8c7a6 72%,#c7b08a 100%)}
.slider h1{position:absolute;top:12px;width:100%;text-align:center;font-family:"Arimo",Arial,sans-serif;font-weight:700;font-size:33px;color:var(--white)}
.arrow{top:128px;width:30px;height:30px;background:#111;display:flex;align-items:center;justify-content:center}
.card{background:#f7f7f5;border:1px solid #c8c8c8;box-shadow:0 1px 3px rgba(0,0,0,.25)}
.head-bar{height:32px;font-family:"Francois One",Arial,sans-serif;font-size:17px;color:var(--white);padding:5px 9px}
.btn{font-size:10px;color:var(--ink);background:linear-gradient(#ffd94a,#f7a800);border:1px solid #c98a00;padding:4px 9px}
.video{left:8px;width:172px;height:86px;border:3px solid var(--white);box-shadow:0 0 2px #999}
.welcome h2{font-family:"Tinos",serif;font-weight:400;font-size:19px;color:var(--ink)}
.welcome h2 small{font-size:14px}
.welcome p{font-size:9.6px;line-height:14.5px;margin-top:10px;color:#333}
.cta{left:256px;top:816px;font-family:"Francois One",Arial,sans-serif;font-size:21px;color:var(--orange-deep);text-decoration:underline;display:flex;align-items:center;gap:6px}
.testimonials{padding:10px 12px 0}
.quote{font-size:9.3px;line-height:13px;color:var(--muted)}
.byline{font-size:9.5px;line-height:12px;color:var(--ink);border-top:1px dashed #777;padding-top:10px;margin-top:12px;white-space:nowrap}
.quote + .quote,.byline + .quote{margin-top:8px}
.login{left:10px;top:890px;width:759px;height:102px;background:var(--green);border:3px solid var(--white);box-shadow:0 1px 3px rgba(0,0,0,.3)}
.login-title{left:0;top:0;width:108px;height:96px;background:linear-gradient(90deg,#6fb31c,#79bd22);box-shadow:3px 0 5px rgba(0,0,0,.2);font-family:"Francois One",Arial,sans-serif;font-size:17px;color:var(--white);padding:32px 0 0 20px;line-height:20px}
.login p{left:118px;top:6px;width:630px;font-size:10.4px;color:var(--white);line-height:13px}
.field{font-size:9.5px;font-weight:700;color:var(--white)}
.input{height:18px;width:172px;background:var(--white);border:1px solid #999;font-size:9px;color:#999;padding:3px 5px;margin-top:3px}
.tile{top:1004px;height:106px;border:3px solid var(--white);box-shadow:0 1px 3px rgba(0,0,0,.3)}
.tile.orange{background:var(--orange-box);color:var(--white);padding:4px 7px}
.tile h3{font-family:"Francois One",Arial,sans-serif;font-weight:400;font-size:16px;line-height:18px}
.tile .date{font-size:9.5px;font-weight:700;color:var(--ink);margin-top:1px}
.tile .body{font-size:9.5px;color:var(--ink);line-height:12px}
.tile .more{position:absolute;right:8px;bottom:5px;font-size:8.5px;font-weight:700;color:var(--ink);text-decoration:underline}
.footer{left:0;top:1127px;width:777px;height:73px;background:var(--footer);color:var(--white);font-size:10.5px}
.footer .hl{color:var(--yellow)}
.social{display:flex;gap:6px;margin-top:8px}
.social div{display:flex;flex-direction:column;align-items:center;font-size:7px;color:#ccc;gap:2px}
.social i{width:22px;height:22px;border-radius:50%;background:#e8eef5;display:block}
</style>
</head>
<body>
<div class="abs top-zone"></div>
<div class="abs side-leaf" style="left:0"></div>
<div class="abs side-leaf" style="right:0"></div>

<header>
  <div class="abs brand">
    <div class="brand-mark"></div>
    <div>
      <div class="brand-name">Peartreegrove</div>
      <div class="brand-sub">BALANCED NUTRITION, MIND, AND FITNESS</div>
    </div>
  </div>
  <div class="abs tagline">The fastest way to get a new life, <a href="#">Fill Up HH Form</a></div>
  <div class="abs search">Search
    <svg width="18" height="18" viewBox="0 0 18 18"><circle cx="10" cy="7" r="5" fill="none" stroke="#222" stroke-width="2"/><line x1="6.5" y1="10.5" x2="2" y2="15" stroke="#222" stroke-width="2.5"/></svg>
  </div>
</header>

<div class="abs stage"></div>
<nav class="abs nav">
  <div class="nav-item active">PROGRAM<small>Your coaching Program</small></div>
  <div class="nav-item">COACH<small>Why need one</small></div>
  <div class="nav-item">RECEIPE<small>Rules to follow</small></div>
  <div class="nav-item">ABOUT<small>About your coach</small></div>
  <div class="nav-item">WORKOUTS<small>Body &amp; Mind</small></div>
</nav>

<div class="abs thumb" style="left:23px"><div class="ph" role="img" aria-label="Waist with measuring tape" style="background:linear-gradient(90deg,#f3e3d6,#fff)"><svg class="play" width="24" height="24"><circle cx="12" cy="12" r="11" fill="#5cb82a" stroke="#fff" stroke-width="2"/><path d="M9 7l8 5-8 5z" fill="#fff"/></svg><span>HEALTH CLASS</span></div></div>
<div class="abs thumb" style="left:172px"><div class="ph" role="img" aria-label="Woman stretching outdoors" style="background:linear-gradient(180deg,#7ab0de,#d7c2a8)"><svg class="play" width="24" height="24"><circle cx="12" cy="12" r="11" fill="#5cb82a" stroke="#fff" stroke-width="2"/><path d="M9 7l8 5-8 5z" fill="#fff"/></svg><span class="g">CIRCUIT TRAINING</span></div></div>
<div class="abs thumb" style="left:319px"><div class="ph" role="img" aria-label="Portrait of a coach" style="background:linear-gradient(90deg,#e6e9ee,#c9d0da)"><svg class="play" width="24" height="24"><circle cx="12" cy="12" r="11" fill="#5cb82a" stroke="#fff" stroke-width="2"/><path d="M9 7l8 5-8 5z" fill="#fff"/></svg><span>BALENCED DIET</span></div></div>
<div class="abs thumb" style="left:467px"><div class="ph" role="img" aria-label="Woman stretching outdoors" style="background:linear-gradient(180deg,#7ab0de,#d7c2a8)"><svg class="play" width="24" height="24"><circle cx="12" cy="12" r="11" fill="#5cb82a" stroke="#fff" stroke-width="2"/><path d="M9 7l8 5-8 5z" fill="#fff"/></svg><span class="g">CIRCUIT TRAINING</span></div></div>
<div class="abs thumb" style="left:615px"><div class="ph" role="img" aria-label="Portrait of a coach" style="background:linear-gradient(90deg,#e6e9ee,#c9d0da)"><svg class="play" width="24" height="24"><circle cx="12" cy="12" r="11" fill="#5cb82a" stroke="#fff" stroke-width="2"/><path d="M9 7l8 5-8 5z" fill="#fff"/></svg><span>BALENCED DIET</span></div></div>

<section class="abs slider" role="img" aria-label="Group doing yoga stretches on a tropical beach">
  <h1>Enjoy Life To The Fullest</h1>
  <div class="abs arrow" style="left:2px"><svg width="10" height="14"><path d="M8 1L2 7l6 6" fill="none" stroke="#fff" stroke-width="2.5"/></svg></div>
  <div class="abs arrow" style="right:2px"><svg width="10" height="14"><path d="M2 1l6 6-6 6" fill="none" stroke="#fff" stroke-width="2.5"/></svg></div>
</section>

<aside class="abs card" style="left:10px;top:608px;width:188px;height:268px">
  <div class="head-bar" style="margin:6px 6px 0;background:linear-gradient(#ffa733,#f07a0c)">VIDEOS</div>
  <div class="abs video" style="top:48px" role="img" aria-label="Smiling woman holding fruit"><div style="width:100%;height:100%;background:linear-gradient(90deg,#f0e6dc,#fff);position:relative"><svg style="position:absolute;left:74px;top:30px" width="24" height="24"><circle cx="12" cy="12" r="11" fill="#5cb82a" stroke="#fff" stroke-width="2"/><path d="M9 7l8 5-8 5z" fill="#fff"/></svg></div></div>
  <div class="abs video" style="top:144px" role="img" aria-label="Woman with raised arms by the sea"><div style="width:100%;height:100%;background:linear-gradient(180deg,#b9cfe6,#6e8ea8 60%,#6b5a45);position:relative"><svg style="position:absolute;left:74px;top:30px" width="24" height="24"><circle cx="12" cy="12" r="11" fill="#5cb82a" stroke="#fff" stroke-width="2"/><path d="M9 7l8 5-8 5z" fill="#fff"/></svg></div></div>
  <div class="abs btn" style="right:8px;bottom:6px">More Videos</div>
</aside>

<article class="abs welcome" style="left:206px;top:614px;width:344px">
  <h2><small>Welcome to</small> Our Happy Health World</h2>
  <p>Lorem ipsum dolor sit amet, consectetur adipiscing elit. Suspendisse scelerisque accumsan ultrices. Quisque felis erat, egestas nec varius sed, tristique eu augue. Vestibulum rutrum, dui nec semper aliquet, neque mauris condimentum massa, vitae viverra lorem lacus quis nisl. Nullam tincidunt suscipit auctor.</p>
  <p>Proin eget nulla ut sem pellentesque hendrerit. Lorem ipsum dolor sit amet, consectetur adipiscing elit. Suspendisse scelerisque accumsan ultrices. Quisque felis erat, egestas nec varius sed, tristique eu augue. Vestibulum rutrum, dui nec semper aliquet, neque mauris condimentum massa, vitae viverra lorem lacus quis nisl. Nullam tincidunt suscipit auctor. Etiam ac quam nisl, eu consectetur lectus. Aliquam ullamcorper, risus id egestas malesuada.</p>
</article>
<a class="abs cta" href="#"><svg width="20" height="20"><circle cx="10" cy="10" r="8.5" fill="none" stroke="#f26a0f" stroke-width="2"/><path d="M6 10h7M10 6.5l3.5 3.5-3.5 3.5" fill="none" stroke="#f26a0f" stroke-width="2"/></svg>Contact Your Health Coach</a>

<aside class="abs card" style="left:562px;top:608px;width:207px;height:268px">
  <div class="head-bar" style="margin:6px 6px 0;background:linear-gradient(#8fd13a,#6bb01a)">WHAT CLIENT SAYS</div>
  <div class="testimonials">
    <p class="quote">Lorem ipsum dolor sit amet, consec tetur adipiscing elit. Susp endisse sceleri que accumsan ultrices. Quisque felis erat, egestas nec.</p>
    <p class="byline">By Owen Hart, CEO Brightmoor Co</p>
    <p class="quote">Proin eget nulla ut sem pellentesque hendrerit. Lorem ipsum dolor sit amet, consectetur adipiscing elit. Suspendis se scelerisque accumsan ultrices.</p>
    <p class="byline">By Lena Voss, CEO Corwell House</p>
  </div>
  <div class="abs btn" style="right:8px;bottom:6px">More Testomonials</div>
</aside>

<section class="abs login">
  <div class="abs login-title">CLIENT<br>LOGIN</div>
  <p class="abs">Get your free login to access to monthly newsletter and archived articles (anyone) as well as teleconferences – to access videos , that privilege is for clients only (please submit your e-mail address and client Number) – thanks!</p>
  <div class="abs" style="left:120px;top:44px"><div class="field">User Id</div><div class="input">User id</div></div>
  <div class="abs" style="left:299px;top:44px"><div class="field">Password</div><div class="input">••••••••••••••••</div></div>
  <div class="abs btn" style="left:480px;top:58px;padding:3px 9px">Login</div>
  <div class="abs" style="left:537px;top:62px;font-size:9.5px;color:var(--white)">Forgot password? <u>Click here</u></div>
</section>

<div class="abs tile" style="left:10px;width:143px;background:linear-gradient(180deg,#6d8aa8,#3f4a3a)" role="img" aria-label="Group of community members smiling together">
  <div class="abs" style="left:0;right:0;bottom:6px;text-align:center;font-family:'Francois One',Arial,sans-serif;font-size:13px;line-height:14px;color:var(--yellow)">Peartreegrove<br>COMMUNITY</div>
</div>
<div class="abs tile orange" style="left:163px;width:145px">
  <h3 style="font-size:12px;line-height:13px">Subscribe</h3>
  <h3 style="color:var(--ink);font-size:17px">NEWSLETTER</h3>
  <div class="input" style="width:124px;margin-top:6px">Type your email id</div>
  <div class="abs" style="left:7px;top:72px;background:linear-gradient(#8fd13a,#5da815);border:1px solid #3f7d0c;color:var(--ink);font-weight:700;font-size:12px;padding:2px 8px">Submit</div>
</div>
<div class="abs tile orange" style="left:317px;width:145px">
  <h3>CALENDAR</h3>
  <div class="date">22st August, 2012</div>
  <div class="body">Proin eget nulla ut sem pellent esque hendrerit. Lorem ipsum dolor sit amet.</div>
  <div class="more">More Events</div>
</div>
<div class="abs tile orange" style="left:471px;width:146px">
  <h3>FORUM</h3>
  <div class="date">22st August, 2012</div>
  <div class="body">Proin eget nulla ut sem pellent esque hendrerit. Lorem ipsum dolor sit amet.</div>
  <div class="more">More Forum Posts</div>
</div>
<div class="abs tile" style="left:625px;width:144px;background:var(--green);color:var(--white)">
  <svg class="abs" style="left:8px;top:12px" width="34" height="40" viewBox="0 0 34 40"><path d="M17 2L32 7v12c0 10-7 16-15 19C9 35 2 29 2 19V7z" fill="#9fd0e8" stroke="#fff" stroke-width="2"/></svg>
  <div class="abs" style="right:7px;top:12px;text-align:right;font-family:'Francois One',Arial,sans-serif;font-size:16px;line-height:16px">HEALTH<br>HISTORY<br>FORMS</div>
  <div class="abs" style="left:10px;top:72px;font-size:10px;line-height:12px;color:var(--ink)">Click here to download your health history form</div>
</div>

<footer class="abs footer">
  <div class="abs" style="left:18px;top:12px">Contact Us:<div style="margin-top:8px;font-size:9.5px;line-height:13px">Mail id : <span class="hl">mara@peartreegrove.example</span><br>Phone: <span class="hl">407-555-0142</span></div></div>
  <div class="abs" style="left:331px;top:12px">Follow Us:
    <div class="social"><div><i></i>friendloom</div><div><i></i>chirpwell</div><div><i></i>linkmesh</div></div>
  </div>
  <div class="abs" style="left:586px;top:12px">Copyright<div class="hl" style="margin-top:8px;font-size:9.5px;line-height:13px">Peartreegrove,<br>©2012, All Rights Reserved</div></div>
</footer>
</body>
</html>
```